Quillmont Renovations Letterhead

Quillmont does not do actual renovation, but rather handles high end project management of renovation (primarily residential with an eye toward commercial and International) The renovation work could look very different between projects. This company works directly with the clients and manages the work of contractors, architects and interior designers (either subcontracted directly by Quillmont or hired by the client and entrusted to Quillmont to manage). Clients are high end in the economic scale and all materials should speak to that audience. Provoke a sense of change, openness and imagination, trust and integrity. The owner is female, but the audience will be heavily slanted male. It should not be a "feminine" or "masculine" looking . If anything, slant more on the masculine side.

Clean, simple, yet creative and artistically appealing. The logo should be clear and not competing with too many surrounding design elements.

There is a contest also on for business card. Please check that section if you would like to compete for both.

Get your creative juices going!

Target Market(s)

High end cients. Additional audience: professionals (architects, etc...) designers, contractors

Industry/Entity Type

Residential

Requirements
Must have
• Logo must be included in all materials

```html
<!DOCTYPE html>
<html lang="en">
<head>
<meta charset="utf-8">
<title>Quillmont Renovations Letterhead</title>
<link rel="stylesheet" href="https://fonts.googleapis.com/css2?family=Arimo:wght@400;700&family=Questrial&display=swap">
<style>
  :root {
    --backdrop: #e4e4e4;
    --paper: #ffffff;
    --ink: #3a3a3a;
    --ink-soft: #555555;
    --brand-ink: #2f3436;
    --accent: #5bbfb4;
  }
  * { box-sizing: border-box; margin: 0; padding: 0; }
  html, body {
    width: 1200px;
    height: 1200px;
    overflow: hidden;
    background: var(--backdrop);
  }
  .letterhead {
    position: absolute;
    left: 175px;
    top: 50px;
    width: 850px;
    height: 1100px;
    background: var(--paper);
    box-shadow: 0 2px 10px rgba(0,0,0,0.12);
    font-family: "Arimo", Arial, sans-serif;
    color: var(--ink);
    font-size: 14px;
    line-height: 1.3;
  }
  .brand {
    position: absolute;
    top: 78px;
    left: 0;
    width: 100%;
    display: flex;
    flex-direction: column;
    align-items: center;
    gap: 14px;
  }
  .brand-mark {
    width: 22px;
    height: 22px;
    background: var(--accent);
  }
  .brand-name {
    font-family: "Questrial", "Century Gothic", sans-serif;
    font-size: 22px;
    letter-spacing: 1.5px;
    color: var(--brand-ink);
    text-transform: uppercase;
  }
  .recipient {
    position: absolute;
    top: 200px;
    left: 100px;
  }
  .recipient .label { margin-bottom: 22px; }
  .recipient .phone { margin-top: 22px; }
  .sender {
    position: absolute;
    top: 232px;
    right: 100px;
    text-align: right;
  }
  .sender .contact { margin-top: 22px; }
  .letter-body {
    position: absolute;
    top: 365px;
    left: 100px;
    right: 100px;
  }
  .subject {
    font-weight: 700;
    color: var(--ink);
    margin-bottom: 22px;
  }
  .letter-body p.paragraph {
    text-align: justify;
    color: var(--ink-soft);
    margin-bottom: 20px;
  }
  .closing {
    position: absolute;
    top: 840px;
    left: 100px;
    color: var(--ink-soft);
  }
  .signature {
    position: absolute;
    top: 945px;
    left: 100px;
    color: var(--ink-soft);
  }
</style>
</head>
<body>
  <main class="letterhead">
    <header class="brand">
      <span class="brand-mark" aria-hidden="true"></span>
      <span class="brand-name">Quillmont Renovations</span>
    </header>

    <section class="recipient">
      <p class="label">To:</p>
      <p>Corvell Company</p>
      <p>Address 4410, Oregon</p>
      <p class="phone">+022 555 0143</p>
    </section>

    <section class="sender">
      <p>Harbor Lane Street</p>
      <p>Boston, USA</p>
      <div class="contact">
        <p>+012 555 0178</p>
        <p>hello@quillmont.com</p>
        <p>www.quillmont.com</p>
      </div>
    </section>

    <article class="letter-body">
      <p class="subject">Lorem ipsum dolor sit amet, consectetur adipiscing elit. Donec a sollicitudin augue.</p>
      <p class="paragraph">Proin malesuada imperdiet felis non rhoncus. Nam ac diam luctus, volutpat lorem ut, condimentum leo. Fusce cursus vulputate eros, at lacinia dui aliquet et. Duis in augue volutpat, laoreet lectus et, porta est. Mauris in mauris vel justo aliquam laoreet id at augue. Morbi iaculis id felis nec varius. Vivamus cursus quam sit amet suscipit dapibus. Pellentesque gravida tempor malesuada. Vivamus ultrices, tellus at consectetur luctus, libero nunc ullamcorper odio, vitae pretium elit tellus at risus. Proin auctor eu massa non posuere. In sed consectetur eros. Quisque erat quam, accumsan sed leo vel, porttitor tempus lorem. Ut rutrum rhoncus posuere.</p>
      <p class="paragraph">Mauris dictum lectus augue, nec feugiat neque dictum vitae. Duis eleifend congue orci, in ultrices magna dignissim quis. Vivamus vitae nisi mi. Aliquam feugiat orci sed risus consectetur ultrices. Phasellus commodo nunc ac odio dapibus vehicula. Pellentesque habitant morbi tristique senectus et netus et malesuada fames ac turpis egestas.</p>
      <p class="paragraph">Nulla adipiscing sodales elit. Cras quis mi auctor, tempor lectus ac, suscipit nisl. Maecenas a suscipit enim. Donec mauris sapien, tincidunt congue fermentum laoreet, vehicula at enim.</p>
      <p class="paragraph">Donec aliquet diam id felis aliquam, nec mattis tellus pulvinar. Vivamus bibendum ante at elit consectetur lacinia.</p>
    </article>

    <p class="closing">Dolor amet,</p>
    <p class="signature">Evan Hale</p>
  </main>
</body>
</html>
```